Website for Bramblewood Quarry Advisors

Please design a website that initially contains four or five pages. This work is for a newly formed consulting company, Bramblewood Quarry Advisors, that provides training and individual coaching to help business professionals and lawyers write more effectively and efficiently.

We work in a professional and conservative industry. The website should be simple, crisp, and clean.

I have attached a document that describes the four initial pages for the site: 1) a landing page, 2) a webpage that includes the pictures and bios of our two consultants, 3) a webpage that describes our services, and 4) a webpage that will contain a form that visitors can use to submit questions to us.

I also included the following files:
a. a powerpoint slide with our consultants' pictures and bios; and
b. our recently designed logo (jpg and png files).

Thank you!

```html
<!DOCTYPE html>
<html lang="en">
<head>
<meta charset="utf-8">
<title>Bramblewood Quarry Advisors</title>
<link href="https://fonts.googleapis.com/css2?family=Poppins:wght@400;500;600&family=Tinos:wght@700&display=swap" rel="stylesheet">
<style>
:root{
  --red:#c8232c;
  --ink:#1a1a1a;
  --body:#555;
  --muted:#8a8a8a;
  --panel:#f3f3f3;
  --white:#fff;
  --footer:#000;
  --serif:"Tinos", "Times New Roman", serif;
  --sans:"Poppins", Arial, sans-serif;
}
*{margin:0;padding:0;box-sizing:border-box}
html,body{width:1200px;height:4065px;overflow:hidden}
body{position:relative;font-family:var(--sans);color:var(--ink);background:var(--white)}
.abs{position:absolute}

/* header */
.site-header{position:absolute;left:0;top:0;width:1200px;height:109px;background:var(--white)}
.brand{position:absolute;left:80px;top:50px;font-family:var(--serif);font-size:20px;font-weight:700;color:var(--ink);display:flex;align-items:center;gap:10px}
.brand-dot{width:10px;height:10px;border-radius:50%;background:var(--red)}
.main-nav{position:absolute;top:49px;left:0;width:1200px;font-size:12px;font-weight:400;color:#333}
.main-nav span{position:absolute;white-space:nowrap}
.main-nav .active{color:var(--red)}
.main-nav .active::after{content:"";position:absolute;left:-4px;right:-4px;top:25px;height:2px;background:var(--red)}

/* hero */
.hero{position:absolute;left:0;top:109px;width:1200px;height:631px;background:linear-gradient(100deg,#6d6761 0%,#8a837b 35%,#5f5953 70%,#3f3a36 100%)}
.hero-title{position:absolute;left:0;width:1200px;top:200px;text-align:center;font-family:var(--serif);font-size:57px;font-weight:700;color:var(--white)}
.hero-text{position:absolute;left:260px;width:680px;top:290px;text-align:center;font-size:14px;line-height:24px;color:#eee;font-weight:500}
.btn{position:absolute;background:var(--red);color:var(--white);font-weight:500;display:flex;align-items:center;justify-content:center;text-transform:uppercase}
.hero .btn{left:505px;top:396px;width:190px;height:58px;font-size:14px}
.slider-dots{position:absolute;left:576px;top:535px;display:flex;gap:4px}
.slider-dots i{width:12px;height:12px;border-radius:50%;background:#aaa}
.slider-dots i:first-child{background:var(--white)}

/* about */
.about{position:absolute;left:0;top:740px;width:1200px;height:589px;background:var(--panel)}
.about-frame{position:absolute;left:110px;top:81px;width:370px;height:408px;border:2px solid var(--red)}
.about-photo{position:absolute;left:129px;top:98px;width:370px;height:409px;background:linear-gradient(90deg,#cfcac3,#ebe8e3 45%,#f4f2ef)}
.section-heading{font-family:var(--serif);font-weight:700;color:var(--ink)}
.rule{display:block;height:3px;background:var(--red)}
.about h2{position:absolute;left:564px;top:128px;font-size:35px}
.about .rule{position:absolute;left:564px;top:178px;width:84px;height:2px}
.about p{position:absolute;left:564px;top:218px;width:524px;font-size:12.4px;line-height:27px;color:var(--body);text-align:justify}
.about .btn{left:564px;top:410px;width:154px;height:58px;font-size:13px}

/* consultants */
.centered-heading{position:absolute;left:0;width:1200px;text-align:center;font-size:52px}
.centered-rule{position:absolute;left:560px;width:80px;height:3px;background:var(--red)}
.bio-name{position:absolute;font-family:var(--serif);font-weight:700;font-size:35px}
.avatar{position:absolute;width:74px;height:74px;border-radius:50%;background:radial-gradient(circle at 50% 40%,#c9a98e,#8a6d58);box-shadow:0 10px 20px rgba(0,0,0,.12)}
.bio{position:absolute;font-size:12.4px;line-height:27px;color:var(--body);text-align:justify}
.bio.right{text-align-last:right}

/* services */
.services{position:absolute;left:0;top:2222px;width:1200px;height:668px;background:var(--panel)}
.card{position:absolute;top:192px;width:248px;text-align:center}
.card-img{width:248px;height:196px}
.card h3{font-size:19px;font-weight:500;line-height:23px;color:var(--ink);margin:20px 10px 10px}
.card p{font-size:11.4px;line-height:20px;color:var(--body);padding:0 18px;text-align:justify;text-align-last:center}
.card .more{position:absolute;left:0;width:248px;top:375px;font-size:12.5px;color:var(--red);text-decoration:underline;font-weight:500}

/* contact */
.field{position:absolute;background:var(--white);border:1px solid #e6e6e6;box-shadow:0 2px 6px rgba(0,0,0,.06);font-size:17px;color:var(--muted);padding:18px 26px}
.submit{left:493px;top:3515px;width:216px;height:69px;font-size:22px;text-transform:uppercase}

/* footer */
.site-footer{position:absolute;left:0;top:3690px;width:1200px;height:325px;background:var(--footer);color:var(--white)}
.foot-title{position:absolute;top:70px;font-size:18px;font-weight:500}
.foot-title::after{content:"";position:absolute;left:0;top:34px;width:34px;height:2px;background:var(--white)}
.foot-link{position:absolute;left:244px;font-size:13px;display:flex;align-items:center;gap:12px}
.contact-item{position:absolute;left:445px;display:flex;gap:20px;align-items:center;font-size:13px;line-height:16px}
.icon-box{width:28px;height:28px;border:1px solid #fff;border-radius:4px;display:flex;align-items:center;justify-content:center}
.newsletter-text{position:absolute;left:742px;top:149px;width:230px;font-size:13px;line-height:18px}
.news-input{position:absolute;left:742px;top:194px;width:218px;height:33px;background:var(--white)}
.news-btn{left:742px;top:238px;width:109px;height:32px;font-size:11px}
.copy-bar{position:absolute;left:0;top:4015px;width:1200px;height:50px;background:var(--red);color:var(--white);font-size:13px}
.copy-bar span{position:absolute;left:76px;top:16px}
.social{position:absolute;top:10px;width:30px;height:30px;border:1px solid #fff;border-radius:4px}
</style>
</head>
<body>

<header class="site-header">
  <div class="brand"><span>Bramblewood Quarry Advisors</span><span class="brand-dot"></span></div>
  <nav class="main-nav">
    <span class="active" style="left:753px">HOME</span>
    <span style="left:820px">CONSULTANTS ▾</span>
    <span style="left:947px">SERVICES ▾</span>
    <span style="left:1040px">CONTACT US</span>
  </nav>
</header>

<section class="hero" role="img" aria-label="Photo of a hand writing in a notebook beside a coffee cup">
  <h1 class="hero-title">Bramblewood Quarry Advisors</h1>
  <p class="hero-text">Lorem ipsum dolor sit amet, consectetur adipiscing elit, sed do eiusmod tempor incididunt ut labore et dolore magna aliqua. Quis ipsum suspendisse ultrices gravida. Risus commodo viverra maecenas accumsan lacus vel facilisis.</p>
  <div class="btn">Learn more</div>
  <div class="slider-dots"><i></i><i></i><i></i></div>
</section>

<section class="about">
  <div class="about-frame"></div>
  <div class="about-photo" role="img" aria-label="Photo of a smiling consultant holding a notebook"></div>
  <h2 class="section-heading">Bramblewood Quarry Advisors</h2>
  <span class="rule"></span>
  <p>Welcome to Bramblewood Quarry Advisors. We train and coach business professionals and lawyers on strategies and techniques to engage, inform, and persuade their readers. We teach our clients that precisely understanding their readers’ concerns and motivations leads them to select the appropriate tone, to develop the most effective narrative, and to make the complicated judgments necessary for effective written communication.</p>
  <div class="btn">Read more</div>
</section>

<section class="consultants">
  <h2 class="section-heading centered-heading" style="top:1412px">Our consultants</h2>
  <span class="centered-rule" style="top:1477px"></span>

  <h3 class="bio-name" style="left:76px;top:1535px">Marla Penhallow</h3>
  <div class="avatar" style="left:79px;top:1605px" role="img" aria-label="Portrait of Marla Penhallow"></div>
  <p class="bio" style="left:189px;top:1596px;width:913px">Marla Penhallow is an Associate Professor and Director of the Academic Enrichment Program at Harrowgate University School of Law. She has devoted her career in legal education to teaching and counseling students and attorneys, with a focus on developing the fundamental skills to promote success and wellbeing in law school and in the legal profession. Previously, she served as a Professor and Director of Academic Excellence, and most recently as Dean and Associate Dean at Eastmoor Law | Linden Falls. She is a former member of the faculty at Corbel University Law School, a Visiting Professor at Linden Falls College Law School, and a Teaching Fellow at Ashgrove University. She earned a Bachelor of Arts from Wexley University, cum laude, and a Juris Doctor from Halden University Law School. After graduation, she practiced employment law in three northeastern states. For the past twenty years, she has served as a consultant and advisor to major law firms and corporations nationwide in designing and presenting professional development training focusing on legal writing and analysis.</p>

  <h3 class="bio-name" style="right:73px;top:1862px">Desmond Arkwright</h3>
  <div class="avatar" style="left:1052px;top:1928px" role="img" aria-label="Portrait of Desmond Arkwright"></div>
  <p class="bio right" style="left:106px;top:1922px;width:914px">Desmond Arkwright provides legal and business writing consulting services to businesses, business professionals, law firms, and attorneys. He earned a Bachelor of Arts, cum laude, in English from Carrow University, a Master of Fine Arts in creative writing from the University of Westmarch Writers’ Workshop, and a Juris Doctor, cum laude, from Stanmere Law School. At the University of Westmarch, Desmond served as the poetry editor of The Westmarch Quarterly. At Stanmere Law School, he served as treasurer and as an editor of the Stanmere Law Review. Following graduation from Stanmere, Desmond practiced law at Pell &amp; Ostrander LLP in the capital, then at Fairweather, Lowe &amp; Keel LLP in his hometown. After private practice, he worked in the general counsel’s office of Northgate Insurance Solutions and Calderon Industries. Desmond was also dedicated to launching and managing with his sister and mother an ophthalmology practice that provides eye care services to patients at senior living facilities.</p>
</section>

<section class="services">
  <h2 class="section-heading centered-heading" style="top:80px">Our services</h2>
  <span class="centered-rule" style="top:145px"></span>

  <article class="card" style="left:77px">
    <div class="card-img" role="img" aria-label="Photo of a businessman in a suit signing papers" style="background:linear-gradient(135deg,#8e8f94,#c9c5bd 60%,#e6e2da)"></div>
    <h3>Training for twenty or more professionals</h3>
    <p>Lorem ipsum dolor sit amet, con sectetur adipiscing elit. Suspendisse viverra a lectus a congue. Aliquam consequat arcu vitae lectus</p>
    <span class="more">READ MORE</span>
  </article>
  <article class="card" style="left:344px">
    <div class="card-img" role="img" aria-label="Photo of a man writing at a white desk" style="background:linear-gradient(135deg,#f1f1f1,#dcdcdc 55%,#3e4a7a)"></div>
    <h3>Training for cohorts of up to twenty professionals</h3>
    <p>Lorem ipsum dolor sit amet, con sectetur adipiscing elit. Suspendisse viverra a lectus a congue.</p>
    <span class="more">READ MORE</span>
  </article>
  <article class="card" style="left:611px">
    <div class="card-img" role="img" aria-label="Photo of a hand writing notes on paper" style="background:linear-gradient(135deg,#e9dfd6,#f3ede7 50%,#d9c1b0)"></div>
    <h3>Training for cohorts followed by one-hour individual coaching for each participant</h3>
    <p>Lorem ipsum dolor sit amet, con sectetur adipiscing elit.</p>
    <span class="more">READ MORE</span>
  </article>
  <article class="card" style="left:878px">
    <div class="card-img" role="img" aria-label="Photo of a person writing in a notebook next to a phone" style="background:linear-gradient(135deg,#7f7a73,#b4aea6 50%,#6c7382)"></div>
    <h3 style="margin-top:33px;margin-bottom:22px">Individual coaching</h3>
    <p>Lorem ipsum dolor sit amet, con sectetur adipiscing elit. Suspendisse viverra a lectus a congue. Aliquam consequat arcu vitae lectus</p>
    <span class="more">READ MORE</span>
  </article>
</section>

<section class="contact">
  <h2 class="section-heading centered-heading" style="top:2970px">Contact us</h2>
  <span class="centered-rule" style="top:3034px"></span>
  <div class="field" style="left:193px;top:3098px;width:814px;height:62px">Company name:</div>
  <div class="field" style="left:193px;top:3168px;width:396px;height:61px">Contact name:</div>
  <div class="field" style="left:609px;top:3168px;width:398px;height:61px">Contact phone number:</div>
  <div class="field" style="left:193px;top:3238px;width:396px;height:61px">Email address:</div>
  <div class="field" style="left:609px;top:3238px;width:398px;height:61px">Physical address:</div>
  <div class="field" style="left:193px;top:3312px;width:814px;height:181px">Open field:</div>
  <div class="btn submit">Submit</div>
</section>

<footer class="site-footer">
  <h4 class="foot-title" style="left:240px">Quick Links</h4>
  <div class="foot-link" style="top:141px"><svg width="7" height="10"><path d="M1 1l4 4-4 4" stroke="#fff" stroke-width="1.6" fill="none"/></svg>Home</div>
  <div class="foot-link" style="top:168px"><svg width="7" height="10"><path d="M1 1l4 4-4 4" stroke="#fff" stroke-width="1.6" fill="none"/></svg>Consultants</div>
  <div class="foot-link" style="top:195px"><svg width="7" height="10"><path d="M1 1l4 4-4 4" stroke="#fff" stroke-width="1.6" fill="none"/></svg>Services</div>
  <div class="foot-link" style="top:222px"><svg width="7" height="10"><path d="M1 1l4 4-4 4" stroke="#fff" stroke-width="1.6" fill="none"/></svg>Contact Us</div>

  <h4 class="foot-title" style="left:445px">Contact Us</h4>
  <div class="contact-item" style="top:143px">
    <span class="icon-box"><svg width="14" height="14" viewBox="0 0 24 24"><path d="M6 2l4 4-2 3c1 3 4 6 7 7l3-2 4 4-3 4C10 22 2 14 2 5z" fill="#fff"/></svg></span>
    <span>CALL US<br>8012 555 0142</span>
  </div>
  <div class="contact-item" style="top:192px">
    <span class="icon-box"><svg width="14" height="12" viewBox="0 0 24 18"><rect x="1" y="1" width="22" height="16" fill="#fff"/><path d="M1 1l11 9 11-9" stroke="#000" stroke-width="2" fill="none"/></svg></span>
    <span>EMAIL US<br>hello@bramblewoodquarry.com</span>
  </div>
  <div class="contact-item" style="top:240px">
    <span class="icon-box"><svg width="12" height="15" viewBox="0 0 20 26"><path d="M10 1a8 8 0 00-8 8c0 6 8 16 8 16s8-10 8-16a8 8 0 00-8-8z" fill="#fff"/><circle cx="10" cy="9" r="3" fill="#000"/></svg></span>
    <span>Address line Dummy Here<br>Address line Here</span>
  </div>

  <h4 class="foot-title" style="left:742px">Our Newsletter</h4>
  <p class="newsletter-text">Subscribe our newsletter to get the latest news.</p>
  <div class="news-input"></div>
  <div class="btn news-btn">Subscribe</div>
</footer>

<div class="copy-bar">
  <span>Copyright © 2024 All Rights Reserved By Bramblewood Quarry Advisors</span>
  <i class="social" style="left:990px"></i>
  <i class="social" style="left:1026px"></i>
  <i class="social" style="left:1061px"></i>
  <i class="social" style="left:1096px"></i>
</div>

</body>
</html>
```